Healthy juice company needs a branded shipping box

I am looking for a branded box that is 10"x10"x10" in standard brown. This is for the box we ship the juice in.

The box should serve as an advertising platform in itself. We offer a subscription juice service. People get a box of juice delivered every week.

The customer should see the box and feel good about what they ordered because it's something healthy they're doing for themselves. The imagery/wording should reinforce that they're doing something healthy for themselves.

Other people who see the box should be curious enough to look us up and want a box for themselves.

I'd like ONE color in the final print.

I'd like the 4 sides of the box to be printed.

The design is up to you.

Inspiration boxes: Amber Ladle, Tidy Basket, PrintHollow

Target Market(s)

Our customers subscribe to our juice because it helps them eat the fruits and veggies they normally wouldn't. They are typically 30-40yrs old, with families, and are upper middle class.

Industry/Entity Type

Delivery Service

Font styles to use
Sans Serif

Colors
f78f20
9bcb3c
ffffff

Requirements
Must have
• The design should feel clean, bright, happy, casual, and healthy.
• Natural fruits & veggies are part of what we do.
• Has to convey farm fresh, fresh made and locally made through the design.
• Must have website: www.varolipressery.example
Nice to have
• These can optionally be included on the box:
• - "I care about my health."
• - "Drink Juice. Live Healthier."
• The box can be branded "The Pulp Crate" on 1+ sides

```html
<!DOCTYPE html>
<html lang="en">
<head>
<meta charset="utf-8">
<title>Varoli Pressery – The Pulp Crate shipping box</title>
<link rel="stylesheet" href="https://fonts.googleapis.com/css2?family=Mulish:wght@400;600;700;800&display=swap">
<style>
  :root {
    --backdrop: #1b1b1b;
    --kraft: #c79d6c;
    --kraft-shade: #b58b5c;
    --kraft-line: #d9b98f;
    --label-white: #f7f7f5;
    --brand-orange: #f78f20;
    --brand-green: #9bcb3c;
    --leaf-green: #3a8f3a;
    --headline-green: #1f5e2a;
    --ink: #1a1a1a;
    --body-ink: #2b2218;
  }
  * { box-sizing: border-box; margin: 0; padding: 0; }
  html, body { width: 1200px; height: 800px; overflow: hidden; }
  body {
    background: var(--backdrop);
    font-family: "Mulish", Arial, sans-serif;
    color: var(--ink);
    position: relative;
  }

  .box-net {
    position: absolute;
    left: 130px;
    top: 120px;
    display: flex;
    height: 560px;
  }
  .panel {
    position: relative;
    height: 100%;
    background: var(--kraft);
    overflow: hidden;
  }
  .panel-pattern {
    position: absolute;
    inset: 0;
    width: 100%;
    height: 100%;
  }

  /* Side panel */
  .panel-side {
    width: 400px;
    background: var(--kraft-shade);
    border-right: 2px solid #a87f52;
  }
  .side-content {
    position: absolute;
    left: 70px;
    right: 40px;
    top: 40px;
    bottom: 20px;
    display: flex;
    flex-direction: column;
    align-items: center;
  }
  .side-brand-tag {
    width: 150px;
    height: 100px;
    background: rgba(247, 247, 245, 0.55);
    border-radius: 6px;
    display: flex;
    align-items: center;
    justify-content: center;
    margin-bottom: 24px;
  }
  .side-brand-tag .brand-name { font-size: 19px; }
  .side-copy {
    font-size: 10.5px;
    line-height: 1.55;
    color: var(--body-ink);
    text-align: justify;
  }
  .side-copy p + p { margin-top: 14px; }
  .side-slogan {
    margin-top: 26px;
    text-align: center;
    font-weight: 700;
    font-size: 20px;
    line-height: 1.2;
    color: var(--ink);
  }
  .side-tagline {
    margin-top: 8px;
    padding: 4px 6px;
    border-top: 1.5px solid var(--ink);
    border-bottom: 1.5px solid var(--ink);
    font-size: 15px;
    font-weight: 600;
  }
  .side-website {
    position: absolute;
    right: 0;
    bottom: 0;
    font-size: 12px;
    color: var(--body-ink);
  }
  .fruit-wheel {
    position: absolute;
    left: -70px;
    top: 365px;
    width: 120px;
    height: 170px;
    border-radius: 50%;
    background: radial-gradient(circle, var(--brand-green) 0%, #d8c31d 70%);
  }

  /* Front panel */
  .panel-front { width: 540px; }
  .label {
    position: absolute;
    left: 130px;
    top: 10px;
    width: 290px;
    height: 430px;
    background: var(--label-white);
    border-radius: 6px;
    box-shadow: 0 1px 3px rgba(0,0,0,0.25);
    display: flex;
    flex-direction: column;
    align-items: center;
    padding-top: 30px;
  }
  .brand-name {
    font-weight: 700;
    color: var(--brand-orange);
    font-size: 34px;
    letter-spacing: 0.5px;
    white-space: nowrap;
  }
  .label-fruits {
    margin-top: 26px;
    display: flex;
    gap: 60px;
  }
  .label-headline {
    margin-top: 22px;
    text-align: center;
    font-size: 33px;
    font-weight: 800;
    line-height: 1.25;
    color: var(--headline-green);
  }
  .label-tagline {
    margin-top: 14px;
    width: 250px;
    padding: 8px 0;
    text-align: center;
    border-top: 1.5px solid var(--ink);
    border-bottom: 1.5px solid var(--ink);
    font-size: 19px;
    font-weight: 600;
  }
  .front-title {
    position: absolute;
    left: 0;
    right: 0;
    top: 448px;
    text-align: center;
  }
  .front-title h1 {
    font-size: 38px;
    font-weight: 800;
    letter-spacing: 1px;
    color: var(--ink);
  }
  .front-title p {
    font-size: 20px;
    font-weight: 600;
    color: var(--ink);
  }
</style>
</head>
<body>
  <main class="box-net">
    <section class="panel panel-side">
      <svg class="panel-pattern" role="img" aria-label="Faint outline pattern of fruits: cherries, pears, apples, bananas and strawberries" viewBox="0 0 400 560" preserveAspectRatio="none">
        <rect width="400" height="560" fill="var(--kraft-shade)"/>
      </svg>
      <div class="fruit-wheel" role="img" aria-label="Round arrangement of sliced fruit"></div>
      <div class="side-content">
        <div class="side-brand-tag"><span class="brand-name">Varoli Pressery</span></div>
        <div class="side-copy">
          <p>Every bottle in this crate was pressed within a day of harvest, using whole fruits and greens grown on small farms near you. Nothing is added and nothing is heated, so each sip keeps the colour, flavour and goodness the season gave it. Chill, shake and enjoy.</p>
          <p>Your subscription brings a fresh crate to your door every week. Mix greens, roots and sweet fruit to reach your daily servings without the fuss. Return the empty bottles with your next delivery and we will wash, refill and send them back around again.</p>
        </div>
        <div class="side-slogan">Drink Juice.<br>Live Healthier</div>
        <div class="side-tagline">I care about my health</div>
        <div class="side-website">www.varolipressery.example</div>
      </div>
    </section>

    <section class="panel panel-front">
      <svg class="panel-pattern" role="img" aria-label="Faint outline pattern of fruits: cherries, pears, apples, bananas and strawberries" viewBox="0 0 540 560" preserveAspectRatio="none">
        <rect width="540" height="560" fill="var(--kraft)"/>
      </svg>
      <div class="label">
        <span class="brand-name">Varoli Pressery</span>
        <div class="label-fruits">
          <svg width="70" height="100" viewBox="0 0 70 100" role="img" aria-label="Yellow-green pear">
            <rect width="70" height="100" rx="30" fill="#c2c82a"/>
          </svg>
          <svg width="80" height="100" viewBox="0 0 80 100" role="img" aria-label="Green apple">
            <rect y="10" width="80" height="90" rx="38" fill="#7fc23e"/>
          </svg>
        </div>
        <div class="label-headline">Drink Juice.<br>Live Healthier</div>
        <div class="label-tagline">I care about my health</div>
      </div>
      <div class="front-title">
        <h1>The Pulp Crate</h1>
        <p>farm fresh, locally made</p>
      </div>
    </section>
  </main>
</body>
</html>
```